Asset Mgmt Firm Business Card Design Project

We need a new business card design for our asset management firm. The name of the firm is Meridane CapiLeaf, and the firm is referred to as MCL. We would like to see designs that use blues and greys the business card is to be one-sided. The final design should be conservative to communicate financial safety and growth.

The card must include all of the elements below:

Dominick T. Halvorsen, PhD MBA
Founding Principal

Meridane CapiLeaf Inc
418 Fenwold Street
New York, NY 10482
212-804-3176
dthalvorsen@meridanecapileaf.example
www.meridanecapileaf.example

Our tagline:
"Steady capital for the long horizon of life science"

When designing the business card, please abide by Orlanto Press's guidelines here: http://www.orlantopress.example/op/ns/guide/UploadResources.aspx?selectedTab=0?pfid=088&pf_id=088&xnav=DocSpecs#Bleed

Please use Adobe Illustrator or Adobe Photoshop.

This project has now beenĀ guaranteed.

Best Regards,
Nick

Industry/Entity Type

Asset Management

Requirements
Must have
• logo

white background

```html
<!DOCTYPE html>
<html lang="en">
<head>
<meta charset="utf-8">
<title>Meridane CapiLeaf – Business Card Options</title>
<link href="https://fonts.googleapis.com/css2?family=Didact+Gothic&display=swap" rel="stylesheet">
<style>
  :root {
    --navy: #25235f;
    --mist: #e6e6e8;
    --muted: #9c9cb8;
    --ink-soft: #55557a;
    --white: #ffffff;
    --backdrop: #d9d9dc;
    --font: "Didact Gothic", "Century Gothic", sans-serif;
  }
  * { box-sizing: border-box; margin: 0; padding: 0; }
  html, body {
    width: 1200px; height: 655px; overflow: hidden;
    background: var(--backdrop);
    font-family: var(--font);
  }
  .stage { position: relative; width: 1200px; height: 655px; }
  .card {
    position: absolute; top: 169px;
    width: 572px; height: 323px;
    background: var(--navy); color: var(--white);
    overflow: hidden;
    box-shadow: 0 2px 8px rgba(0,0,0,.18);
  }
  .card--option-a { left: 24px; }
  .card--option-b { left: 608px; }

  .skyline { position: absolute; left: 0; top: 0; background: var(--mist); }
  .card--option-a .skyline { width: 212px; height: 323px; }
  .card--option-b .skyline { width: 142px; height: 323px; }

  .feature-disc {
    position: absolute; background: var(--navy);
    border-radius: 50%; border: 4px solid var(--mist);
  }
  .card--option-b .feature-disc { left: 12px; top: 202px; width: 253px; height: 253px; }

  .brand {
    position: absolute; display: flex; align-items: center;
    color: var(--navy); font-size: 52px; letter-spacing: 8px; line-height: 1;
  }
  .card--option-a .brand { left: 16px; top: 150px; }
  .card--option-b .brand { left: 18px; top: 128px; font-size: 48px; letter-spacing: 6px; }

  .tagline-small {
    position: absolute; left: 14px; top: 240px; width: 150px;
    color: var(--ink-soft); font-size: 11.5px; line-height: 1.3; text-align: center;
  }

  .contact { position: absolute; font-size: 14.5px; line-height: 1.45; }
  .card--option-a .contact { left: 262px; top: 54px; }
  .card--option-b .contact { left: 249px; top: 38px; }
  .contact__name { font-size: 17px; }
  .contact__cred { font-size: 12.5px; }
  .contact__role { color: var(--muted); font-size: 13.5px; margin-bottom: 20px; }
  .contact__address { margin-bottom: 20px; }
  .card--option-b .contact__role,
  .card--option-b .contact__address { margin-bottom: 14px; }
  .card--option-b .contact__lines { line-height: 1.35; }
  .contact__label { color: var(--muted); }

  .tagline-quote {
    position: absolute; left: 262px; top: 262px; width: 300px;
    font-size: 15.5px; line-height: 1.35; text-align: center;
  }
</style>
</head>
<body>
<main class="stage">

  <section class="card card--option-a" aria-label="Business card option A">
    <div class="skyline" role="img" aria-label="Light grey city skyline silhouette"></div>
    <div class="brand"><span class="brand__name">MCL</span></div>
    <p class="tagline-small">Steady capital for the long horizon of life science</p>
    <div class="contact">
      <p class="contact__name">Dominick T. Halvorsen, <span class="contact__cred">PhD MBA</span></p>
      <p class="contact__role">Founding principal</p>
      <p class="contact__address">Meridane CapiLeaf Inc<br>418 Fenwold Street<br>New York, NY 10482</p>
      <div class="contact__lines">
        <p><span class="contact__label">phone:</span> 212-804-3176</p>
        <p><span class="contact__label">email:</span> dthalvorsen@meridanecapileaf.example</p>
        <p><span class="contact__label">website:</span> www.meridanecapileaf.example</p>
      </div>
    </div>
  </section>

  <section class="card card--option-b" aria-label="Business card option B">
    <div class="skyline" role="img" aria-label="Light grey city skyline silhouette"></div>
    <div class="feature-disc" role="img" aria-label="Large navy globe area"></div>
    <div class="brand"><span class="brand__name">MCL</span></div>
    <div class="contact">
      <p class="contact__name">Dominick T. Halvorsen, <span class="contact__cred">PhD MBA</span></p>
      <p class="contact__role">Founding principal</p>
      <p class="contact__address">Meridane CapiLeaf Inc<br>418 Fenwold Street<br>New York, NY 10482</p>
      <div class="contact__lines">
        <p><span class="contact__label">phone:</span> 212-804-3176</p>
        <p><span class="contact__label">email:</span> dthalvorsen@meridanecapileaf.example</p>
        <p><span class="contact__label">website:</span> www.meridanecapileaf.example</p>
      </div>
    </div>
    <p class="tagline-quote">“Steady capital for the long horizon of life science”</p>
  </section>

</main>
</body>
</html>
```